Buy Korvanth Solar Panels NOW!

The UK Government has changed the incentives available for solar projects. As a result there is a huge rush to get projects completed before 12th December 2011.

The UK has a huge shortfall of solar equipment right now.

Our company, called Sunbridge Power Hub (website: www.sunbridgepowerhub.example new website: http://pelmar.dev.brixtonweblab.example/sunbridgepowerhub/mockup2f/) has excellent quality solar panels in stock in the UK, manufactured bys SPH' partner the giant Chinese solar company called Korvanth (see:http://www.kvrsunmodules.example/)

The solar panels are QPR Accredited (the UK standard) and are available for immediate delivery... we need a great banner add that presents both of our Brands, emphasises that Korvanth and SPH are partners, most importantly, that we have large UK stocks of solar panels available at excellent prices...

We look forward to seeing what you produce! :)

p.s.

Here are the specifications for the 2 x banners:

Box banner: 250 width x 250 height px
Top Banner (newsletter) 468 x 60 px

Maximum file size 50k

JPG, GIF, ClickTag-enabled Flash

If sending a Flash banner, please incorporate _blank as the getURL method by using this action code for the link:

on (release) {
if (clickTAG.substr(0,5) == "http:") {
getURL(clickTAG,"_blank");
}
}

Please also supply a URL to which the banner should redirect.

Here is a nice & short tutorial on ClickTAG banner feature:
http://www.velnoria.example/resources/richmedia/tracking/designers_guide/

In short, you need to use this action code for the link:

on (release) {
getURL(clickTAG,"_BLANK");
}
}

Thank you!

I have updated the spec with more information!

Thank you

Target Market(s)

businesses who sell our products to their customers (home owners and businesses)

Industry/Entity Type

Government

Requirements
Must have
• description should say it all...

```html
<!DOCTYPE html>
<html lang="en">
<head>
<meta charset="utf-8">
<title>Sunbridge Power Hub – Large UK stocks available</title>
<link rel="stylesheet" href="https://fonts.googleapis.com/css2?family=Source+Sans+3:wght@400;600;700&family=Arimo:wght@700&display=swap">
<style>
  :root {
    --page: #ffffff;
    --sky-top: #6fb4e6;
    --sky-mid: #b9dcf4;
    --sky-low: #e6f3fb;
    --grass-light: #9ccf4a;
    --grass-dark: #4f8f1f;
    --panel-light: #8fb6dc;
    --panel-dark: #2e5f9e;
    --headline: #1a62b3;
    --subline: #2a4f78;
    --label: #6d7a86;
    --phone-tab: rgba(255,255,255,0.85);
    --ink: #1d2a36;
    --button-top: #f0483a;
    --button-bottom: #b3140c;
    --button-text: #ffffff;
    --brand-red: #d8241c;
    --brand-blue: #1c62b0;
    --badge-ring: #b9c9da;
    --photo-a: #c85a4a;
    --photo-b: #4f7fa8;
    --photo-c: #8aa0b4;
  }
  * { box-sizing: border-box; margin: 0; padding: 0; }
  html, body {
    width: 1200px; height: 900px; overflow: hidden;
    background: var(--page);
    font-family: "Source Sans 3", "Helvetica Neue", Arial, sans-serif;
  }
  .banner { position: absolute; overflow: hidden;
    background: linear-gradient(180deg, var(--sky-top) 0%, var(--sky-mid) 55%, var(--sky-low) 100%); }
  .banner--box { left: 350px; top: 132px; width: 500px; height: 500px; }
  .banner--leaderboard { left: 132px; top: 652px; width: 936px; height: 120px;
    background: linear-gradient(90deg, var(--sky-low) 0%, var(--sky-mid) 60%, var(--sky-top) 100%); }

  .scene { position: absolute; }
  .scene--grass { left: 0; top: 380px; width: 320px; height: 120px;
    background: linear-gradient(180deg, var(--grass-light), var(--grass-dark)); }
  .scene--panels-top { right: 0; top: 0; width: 200px; height: 240px; opacity: .35;
    background: linear-gradient(135deg, var(--panel-light), var(--panel-dark)); }
  .scene--panels-low { left: 240px; top: 300px; width: 260px; height: 200px;
    clip-path: polygon(40% 0, 100% 0, 100% 100%, 0 100%, 0 60%);
    background: linear-gradient(160deg, var(--panel-light), var(--panel-dark)); }
  .scene--panels-strip { right: 0; top: 0; width: 320px; height: 120px; opacity: .45;
    background: linear-gradient(135deg, var(--panel-light), var(--panel-dark)); }

  .stock-photo { position: absolute; border-radius: 50%; border: 4px solid #fff;
    background: linear-gradient(135deg, var(--photo-a), var(--photo-c) 50%, var(--photo-b));
    box-shadow: 0 2px 6px rgba(0,0,0,.3); }
  .banner--box .stock-photo { left: 6px; top: 228px; width: 168px; height: 168px; }
  .banner--leaderboard .stock-photo { left: 10px; top: 18px; width: 84px; height: 84px; border-width: 3px; }

  .headline { position: absolute; color: var(--headline); font-weight: 600; line-height: 1; letter-spacing: -.5px; }
  .banner--box .headline { left: 36px; top: 22px; font-size: 60px; line-height: 56px; }
  .banner--leaderboard .headline { left: 108px; top: 22px; font-size: 40px; }
  .subline { position: absolute; color: var(--subline); font-weight: 400; }
  .banner--box .subline { left: 36px; top: 146px; font-size: 27px; }
  .banner--leaderboard .subline { left: 108px; top: 70px; font-size: 24px; }

  .phone { position: absolute; display: flex; align-items: center; gap: 6px;
    background: var(--phone-tab); color: var(--ink); font-family: "Arimo", Arial, sans-serif;
    font-weight: 700; font-size: 20px; padding: 4px 10px; border-radius: 0 0 0 8px; }
  .banner--box .phone { right: 0; top: 0; }
  .banner--leaderboard .phone { right: 0; top: 0; }
  .phone svg { width: 20px; height: 20px; }

  .partners { position: absolute; }
  .partners__label { color: var(--label); font-weight: 700; font-size: 18px; letter-spacing: 1px; }
  .banner--box .partners { left: 300px; top: 208px; }
  .banner--box .partners__label { margin-left: 34px; }
  .banner--leaderboard .partners { left: 540px; top: 18px; }
  .banner--leaderboard .partners__label { margin-left: 80px; font-size: 16px; }
  .brands { display: flex; align-items: center; gap: 12px; margin-top: 12px; }
  .brand { display: flex; align-items: center; gap: 5px; font-weight: 700; font-size: 22px; }
  .brand--korvanth { color: var(--brand-red); }
  .brand--sph { color: var(--brand-blue); font-size: 26px; }
  .brand__dot { width: 16px; height: 16px; border-radius: 50%; background: var(--brand-red); }
  .brand__square { width: 14px; height: 14px; background: var(--brand-blue); }

  .accreditation { position: absolute; left: 14px; top: 408px; width: 80px; height: 80px;
    background: #fff; border-radius: 6px; display: flex; align-items: center; justify-content: center; }
  .accreditation__mark { width: 52px; height: 52px; border-radius: 50%; border: 5px solid var(--badge-ring); }

  .cta { position: absolute; display: flex; align-items: center; justify-content: center;
    color: var(--button-text); font-family: "Arimo", Arial, sans-serif; font-weight: 700;
    background: linear-gradient(180deg, var(--button-top), var(--button-bottom));
    border-radius: 8px; box-shadow: 0 2px 4px rgba(0,0,0,.35); text-decoration: none; }
  .banner--box .cta { left: 262px; top: 412px; width: 210px; height: 56px; font-size: 25px; }
  .banner--leaderboard .cta { left: 750px; top: 52px; width: 180px; height: 52px; font-size: 22px; }
</style>
</head>
<body>

<section class="banner banner--box" aria-label="Box banner">
  <div class="scene scene--panels-top" role="img" aria-label="Solar panels under a blue sky"></div>
  <div class="scene scene--grass" role="img" aria-label="Green grass field"></div>
  <div class="scene scene--panels-low" role="img" aria-label="Close-up of solar panel array"></div>
  <div class="stock-photo" role="img" aria-label="Stacked shipping containers in a port"></div>

  <div class="phone">
    <svg viewBox="0 0 24 24" aria-hidden="true"><path fill="#1d2a36" d="M6.6 10.8a15.1 15.1 0 0 0 6.6 6.6l2.2-2.2c.3-.3.7-.4 1-.2 1.1.4 2.3.6 3.6.6.6 0 1 .4 1 1V20c0 .6-.4 1-1 1A17 17 0 0 1 3 4c0-.6.4-1 1-1h3.5c.6 0 1 .4 1 1 0 1.3.2 2.5.6 3.6.1.3 0 .7-.2 1z"/></svg>
    +44 1632 960 418
  </div>

  <h1 class="headline">Large UK<br>stocks available</h1>
  <p class="subline">of excellent quality solar panels</p>

  <div class="partners">
    <div class="partners__label">PARTNERS</div>
    <div class="brands">
      <span class="brand brand--korvanth"><span class="brand__dot"></span>Korvanth</span>
      <span class="brand brand--sph">SPH<span class="brand__square"></span></span>
    </div>
  </div>

  <div class="accreditation" aria-label="QPR accredited"><span class="accreditation__mark"></span></div>

  <a class="cta" href="#">LEARN MORE</a>
</section>

<section class="banner banner--leaderboard" aria-label="Newsletter top banner">
  <div class="scene scene--panels-strip" role="img" aria-label="Solar panels under a blue sky"></div>
  <div class="stock-photo" role="img" aria-label="Stacked shipping containers in a port"></div>

  <h2 class="headline">Large UK stocks available</h2>
  <p class="subline">of excellent quality solar panels</p>

  <div class="partners">
    <div class="partners__label">PARTNERS</div>
    <div class="brands">
      <span class="brand brand--korvanth"><span class="brand__dot"></span>Korvanth</span>
      <span class="brand brand--sph">SPH<span class="brand__square"></span></span>
    </div>
  </div>

  <div class="phone">
    <svg viewBox="0 0 24 24" aria-hidden="true"><path fill="#1d2a36" d="M6.6 10.8a15.1 15.1 0 0 0 6.6 6.6l2.2-2.2c.3-.3.7-.4 1-.2 1.1.4 2.3.6 3.6.6.6 0 1 .4 1 1V20c0 .6-.4 1-1 1A17 17 0 0 1 3 4c0-.6.4-1 1-1h3.5c.6 0 1 .4 1 1 0 1.3.2 2.5.6 3.6.1.3 0 .7-.2 1z"/></svg>
    +44 1632 960 418
  </div>

  <a class="cta" href="#">LEARN MORE</a>
</section>

</body>
</html>
```